Indian Lunch Delivery company needs a google ad banner for advertising its offering

We are a Kolkata, India based startup delivering lunch to office buildings in the city. We only serve set meals (vegetarian and non-vegetarian). Minimum order quantity is 5 boxes. The name of the brand is Verdanix (Thali=platter). Our USP-
We cook fresh
Trans-fat free
No emulsifiers, preservatives or artificial colorings used.
Importantly, we are a value for money brand. To be precise our meals costs just .99 c.
Target Market(s)
Young professionals
Industry/Entity Type
It Company
Font styles to use
Sans Serif
Requirements
Must have
- Home made food feel to it
Nice to have
- Lots of colours

```html
<!DOCTYPE html>
<html lang="en">
<head>
<meta charset="utf-8">
<title>Verdanix – Everyday Healthy</title>
<link rel="stylesheet" href="https://fonts.googleapis.com/css2?family=Oswald:wght@300;400&family=Roboto:wght@400;500&display=swap">
<style>
  :root {
    --teal: #5ec6a1;
    --ink: #333333;
    --grey-mark: #a6a6a6;
    --frame: #8a8a8a;
    --paper: #ffffff;
    --food-warm: #c8622a;
    --food-rice: #e9e2cf;
    --food-dark: #5a2f1a;
  }
  * { margin: 0; padding: 0; box-sizing: border-box; }
  html, body { width: 1200px; height: 232px; overflow: hidden; background: var(--paper); }
  .banner {
    position: relative;
    width: 1200px; height: 232px;
    background: var(--paper);
    border: 1px solid var(--frame);
    border-top: 5px solid var(--teal);
    overflow: hidden;
    font-family: "Roboto", sans-serif;
  }
  .brand {
    position: absolute;
    left: 28px; top: 68px;
    width: 86px; height: 86px;
    border-radius: 50%;
    background: var(--grey-mark);
    display: flex; align-items: center; justify-content: center;
  }
  .brand-name {
    font-weight: 500;
    font-size: 14px;
    letter-spacing: 0.5px;
    color: var(--paper);
    text-transform: uppercase;
  }
  .headline {
    position: absolute;
    left: 456px; top: 58px;
    transform: translateX(-50%);
    white-space: nowrap;
    font-weight: 400;
    font-size: 39px;
    color: var(--teal);
  }
  .tagline {
    position: absolute;
    left: 456px; top: 110px;
    font-family: "Oswald", sans-serif;
    font-weight: 300;
    font-size: 51px;
    line-height: 1.2;
    color: var(--ink);
    letter-spacing: -0.5px;
    white-space: nowrap;
    transform: translateX(-50%) scaleX(0.9);
    transform-origin: center;
  }
  .cta {
    position: absolute;
    left: 804px; top: 93px;
    width: 152px; height: 43px;
    border: 1.5px solid var(--ink);
    display: flex; align-items: center; justify-content: center;
    font-size: 15px;
    color: var(--ink);
    text-decoration: none;
    letter-spacing: 0.3px;
    background: var(--paper);
    z-index: 2;
  }
  .cta-arrow { margin-left: 12px; }
  .food {
    position: absolute;
    left: 840px; top: 0;
    width: 360px; height: 232px;
  }
</style>
</head>
<body>
  <div class="banner">
    <div class="brand"><span class="brand-name">Verdanix</span></div>
    <h1 class="headline">Everyday Healthy</h1>
    <p class="tagline">RECIPES FOR SIMPLE &amp; HEALTHY EATING</p>
    <a class="cta" href="#">ORDER NOW<span class="cta-arrow">&gt;</span></a>
    <svg class="food" viewBox="0 0 360 232" role="img" aria-label="Photo of Indian thali dishes: rice with peas, curries and flatbread in bowls">
      <defs>
        <linearGradient id="foodTones" x1="0" y1="0" x2="1" y2="1">
          <stop offset="0" stop-color="var(--food-rice)"/>
          <stop offset="0.35" stop-color="#d9a06a"/>
          <stop offset="0.7" stop-color="var(--food-warm)"/>
          <stop offset="1" stop-color="var(--food-dark)"/>
        </linearGradient>
      </defs>
      <path d="M5 232 Q2 196 22 186 Q30 158 63 154 Q90 130 126 136 Q146 112 184 104 Q204 80 240 74 Q266 50 310 52 Q334 42 362 44 L362 234 Z"
            fill="url(#foodTones)" stroke="var(--teal)" stroke-width="5" stroke-linejoin="round"/>
    </svg>
  </div>
</body>
</html>
```